Elegant and modern body scrub for organic junkies

I need a package design for my new company based out of Austin, Texas. We are focused on cruelty free and all natural and organic products. Our deign needs to be able to have the information we require on it, while still appearing very clean and captivating. Our initial product is a clear skin body scrub, intended for people with problematic skin. Our target market is women and we want to show elegance, without appearing "high end."
Updates

Reason: I want to allot more time for certain designers to submit edits. Last minute proposals have been appealing

Target Market(s)

Women. Organic and holistic minded. Natural beauty lovers.

Industry/Entity Type

Skin Care Product

Font styles to use
Script
Other font styles liked:
• AmericanTypewriter, Beautifulflaws, courier, caviarDreams-bold

Colors
000000
ffc214
ffffff
fece3e
fbee3e

Requirements
Must have
• Must be designed in Adobe Illustrator.
• The photo titled “structure for oz and grams” -That needs to be included at the bottom of 1B. I like the horizontal and vertical bar that separate the two. I want that.
• Color Inspiration - The photo titled “venra color inspiration” and “color combo inspiration” are the colors I want. BLACK, GOLD, WHITE. I want the label background black and the writing in white with some gold somewhere on it. My logo is going to be a golden elephant.
• The photos titled “I like how clean this looks” and “I also like how clean this looks” - I want 1B to look super clean. I don’t want a lot of information in this box. I want simple and clean. This is where the logo and brand name will go.
• Logo - A golden elephant. I want it to be gold and geometric. There can be dimension like this elephant example on the left of the 1B description. I want the trunk to be facing to the left and the trunk needs to be raised overhead and touching the animal's forehead.
• The photo titled “sideways writing and silver rim” - I want 1C to be written sideways like this. My text will be much more extensive so the font won’t be able to be so big.
Nice to have
• The photo titled “sideways writing and silver rim” - I want 1C to be written sideways like this. My text will be much more extensive so the font won’t be able to be so big. I also REALLY like how this label is rimmed in silver, but I would want gold. This is not mandatory, but I really like this.
• The photo titled “melted honey” - This is another option I really like. The gold that looks like honey dripping on the label is really cool. Not mandatory, but I really liked that. I also like the craft background on this.
• Color Inspiration - The photo titled “color inspiration” and “another color inspiration” is an option I would also like to see. Rather than black, I’d like to see what it would ALSO look like with a navy background. NAVY, GOLD, WHITE, maybe black somewhere.
Should not have
• Colorful patterns or excessive info in section 1B.

```html
<!DOCTYPE html>
<html lang="en">
<head>
<meta charset="utf-8">
<title>Body Scrub Label – Two Variants</title>
<link rel="stylesheet" href="https://fonts.googleapis.com/css2?family=Cinzel:wght@400&family=Lato:ital,wght@0,400;1,400&display=swap">
<style>
  :root {
    --page: #ffffff;
    --marble-dark: #070606;
    --marble-mid: #1a1610;
    --marble-gold: #8a6a1c;
    --panel: #1f1b20;
    --frame-light: #e9e4d8;
    --frame-gold: #b8953e;
    --gold: #d1a935;
    --text-light: #e4e1e3;
    --rule: #6b6670;
  }
  * { margin: 0; padding: 0; box-sizing: border-box; }
  html, body { width: 1200px; height: 1104px; overflow: hidden; background: var(--page); }
  .canvas { position: relative; width: 1200px; height: 1104px; }

  .label {
    position: absolute; left: 252px; width: 658px; height: 350px;
  }
  .label--light-frame { top: 165px; }
  .label--gold-frame { top: 587px; }

  .marble {
    position: absolute; inset: 0;
    background:
      radial-gradient(ellipse at 10% 20%, rgba(138,106,28,.55), transparent 40%),
      radial-gradient(ellipse at 95% 70%, rgba(138,106,28,.5), transparent 35%),
      radial-gradient(ellipse at 60% 95%, rgba(138,106,28,.45), transparent 40%),
      linear-gradient(135deg, var(--marble-dark), var(--marble-mid) 50%, var(--marble-dark));
  }

  .panel {
    position: absolute; left: 33px; width: 592px;
    background: var(--panel);
    display: flex; flex-direction: column; align-items: center;
  }
  .label--light-frame .panel { top: 29px; height: 287px; border: 2px solid var(--frame-light); }
  .label--gold-frame .panel { top: 28px; height: 290px; border: 1.5px solid var(--frame-gold); }

  .mark {
    display: flex; align-items: center; gap: 8px;
    font-family: "Cinzel", serif; font-size: 16px; letter-spacing: 3px;
    color: var(--gold);
  }
  .mark__dot { width: 10px; height: 10px; border-radius: 50%; background: var(--gold); }
  .label--light-frame .mark { margin-top: 95px; }
  .label--gold-frame .mark { margin-top: 108px; }

  .brand-name {
    font-family: "Cinzel", serif; font-weight: 400; color: var(--text-light);
    word-spacing: 14px; line-height: 1;
  }
  .label--light-frame .brand-name { font-size: 40px; margin-top: 24px; }
  .label--gold-frame .brand-name { font-size: 34px; margin-top: 24px; }

  .net-weight {
    position: absolute; display: flex; font-family: "Lato", sans-serif;
    color: var(--text-light); border-top: 1px solid var(--rule);
  }
  .net-weight__cell { flex: 1; text-align: center; padding-top: 6px; }
  .net-weight__cell + .net-weight__cell { border-left: 1px solid var(--rule); }

  .label--light-frame .net-weight { left: 234px; top: 253px; width: 116px; height: 20px; font-size: 9px; }
  .label--gold-frame .net-weight { left: 132px; top: 253px; width: 321px; height: 28px; font-size: 9px; font-style: italic; }
</style>
</head>
<body>
<main class="canvas">

  <section class="label label--light-frame">
    <div class="marble" role="img" aria-label="Black marble texture with gold veins"></div>
    <div class="panel">
      <div class="mark"><span class="mark__dot"></span><span>VENRA</span></div>
      <h1 class="brand-name">BRAND NAME</h1>
      <div class="net-weight">
        <span class="net-weight__cell">12OZ</span>
        <span class="net-weight__cell">340 g</span>
      </div>
    </div>
  </section>

  <section class="label label--gold-frame">
    <div class="marble" role="img" aria-label="Black marble texture with gold veins"></div>
    <div class="panel">
      <div class="mark"><span class="mark__dot"></span><span>VENRA</span></div>
      <h2 class="brand-name">BRAND NAME</h2>
      <div class="net-weight">
        <span class="net-weight__cell">12OZ</span>
        <span class="net-weight__cell">340 g</span>
      </div>
    </div>
  </section>

</main>
</body>
</html>
```